Photography business - business card design quick turn around

Create a business card design for me please. I actually need the final design back before the end of Sunday 13th May 7pm GMT. Sorry for the short notice.

Photoshop artwork template uploaded with artwork guidelines including printer profiles and other mandatory specifications. Only one side of the business card is required as the other side will be an image.

The design is required as an unflattened PSD file so that I can edit the text if I need to.

My brand colours are white and the teal you see in the logo. Occasionally I also use a dark grey on my website (I don't mind the shade of grey as appreciate grey on teal would be a different grey, to the grey I use on white on the website, so just use a shade of grey that matches). Font can be as the font for the logo or if you prefer I am open to another sans serif, easily legible font. Ideally font size will be 12+.Please do not use capital letters for text. I prefer everything to be lower case, if possible.

Thank you.

Mira

Target Market(s)

Other business owners who may refer me and families

Industry/Entity Type

Photographer

Contact Information for Business Card

Silver Lantern Photography Logo
Sub text: family portraiture, captured with love

Contact information, ideally using simple icons to represent email / website / facebook / instagram / pinterest

email: mira@silverlanternphotography.co.uk
website: silverlanternphotography.co.uk
facebook: @silverlanternphotography
pinterest: @silverlanternph
instagram: @silverlantern_photography
mobile/telephone: 07931460217

If there is too much text then please drop the instagram and pinterest information.

Font styles to use
Sans Serif

Colors
33b8a4

Requirements
Must have
• Logo
• Contact details as listed above
• sub text
Nice to have
• Instagram and Pinterest contact details
• Nice to have icons to represent website / phone / facebook etc followered by the handle where relevant

```html
<!DOCTYPE html>
<html lang="en">
<head>
<meta charset="utf-8">
<title>Silver Lantern Photography – business card</title>
<link href="https://fonts.googleapis.com/css2?family=Montserrat:wght@400;500;600&display=swap" rel="stylesheet">
<style>
  :root {
    --teal: #44bfb0;
    --teal-dark: #33b8a4;
    --white: #ffffff;
    --grey: #7a7a7a;
    --grey-dark: #555555;
    --backdrop: #e4e6e6;
  }
  * { box-sizing: border-box; margin: 0; padding: 0; }
  html, body {
    width: 1200px; height: 880px; overflow: hidden;
    background: var(--backdrop);
    font-family: "Montserrat", Arial, sans-serif;
  }
  .canvas { position: relative; width: 1200px; height: 880px; }

  .card {
    position: absolute;
    width: 540px; height: 310px;
    border-radius: 26px;
    box-shadow: 0 6px 18px rgba(0,0,0,.12);
    overflow: hidden;
  }

  .brand-name {
    font-weight: 500;
    letter-spacing: 1px;
    line-height: 1.15;
    text-transform: uppercase;
  }
  .brand-name .sub {
    display: block;
    text-transform: lowercase;
  }

  /* front */
  .card--front {
    left: 40px; top: 110px;
    background: var(--teal);
    color: var(--white);
    display: flex; flex-direction: column;
    align-items: center; justify-content: center;
    text-align: center;
  }
  .card--front .brand-name { font-size: 28px; }
  .card--front .brand-name .sub { font-size: 14px; letter-spacing: 5px; }
  .tagline {
    margin-top: 30px;
    font-size: 14px;
    font-weight: 500;
    letter-spacing: .6px;
  }

  /* back */
  .card--back {
    left: 620px; top: 460px;
    background: var(--white);
    display: flex; align-items: center;
  }
  .card--back .brand {
    width: 226px;
    padding-left: 34px;
    color: var(--teal-dark);
  }
  .card--back .brand-name { font-size: 20px; }
  .card--back .brand-name .sub { font-size: 11px; letter-spacing: 4px; }
  .divider {
    width: 1px; height: 190px;
    background: var(--teal);
    margin: 0 20px 0 4px;
  }
  .details { flex: 1; min-width: 0; }
  .person-name {
    color: var(--teal-dark);
    font-weight: 600;
    font-size: 16px;
    letter-spacing: .5px;
  }
  .person-role {
    color: var(--grey-dark);
    font-size: 12px;
    margin-bottom: 12px;
  }
  .contact-list { list-style: none; }
  .contact-list li {
    display: flex; align-items: center;
    gap: 8px;
    font-size: 11.5px;
    color: var(--grey);
    margin-bottom: 6px;
    white-space: nowrap;
  }
  .icon { width: 16px; height: 16px; flex: none; }
</style>
</head>
<body>
<div class="canvas">

  <section class="card card--front" aria-label="business card front">
    <div class="brand-name">silver lantern<span class="sub">photography</span></div>
    <p class="tagline">family portraiture, captured with love</p>
  </section>

  <section class="card card--back" aria-label="business card back">
    <div class="brand">
      <div class="brand-name">silver lantern<span class="sub">photography</span></div>
    </div>
    <div class="divider"></div>
    <div class="details">
      <p class="person-name">DANA HOLLIS</p>
      <p class="person-role">Manager</p>
      <ul class="contact-list">
        <li>
          <svg class="icon" viewBox="0 0 16 16"><circle cx="8" cy="8" r="7.2" fill="none" stroke="#33b8a4" stroke-width="1.2"/><rect x="5.5" y="3.8" width="5" height="8.4" rx="1" fill="none" stroke="#33b8a4" stroke-width="1.1"/></svg>
          07931460217
        </li>
        <li>
          <svg class="icon" viewBox="0 0 16 16"><circle cx="8" cy="8" r="7.2" fill="none" stroke="#33b8a4" stroke-width="1.2"/><rect x="4.2" y="5.2" width="7.6" height="5.6" fill="none" stroke="#33b8a4" stroke-width="1.1"/><path d="M4.2 5.2 8 8.3l3.8-3.1" fill="none" stroke="#33b8a4" stroke-width="1.1"/></svg>
          mira@silverlanternphotography.co.uk
        </li>
        <li>
          <svg class="icon" viewBox="0 0 16 16"><circle cx="8" cy="8" r="7.2" fill="none" stroke="#33b8a4" stroke-width="1.2"/></svg>
          @silverlanternphotography
        </li>
        <li>
          <svg class="icon" viewBox="0 0 16 16"><circle cx="8" cy="8" r="7.2" fill="none" stroke="#33b8a4" stroke-width="1.2"/></svg>
          @silverlanternph
        </li>
        <li>
          <svg class="icon" viewBox="0 0 16 16"><circle cx="8" cy="8" r="7.2" fill="none" stroke="#33b8a4" stroke-width="1.2"/></svg>
          @silverlantern_photography
        </li>
      </ul>
    </div>
  </section>

</div>
</body>
</html>
```